Corbel Crest Lighting - Commercial & Residential Landscape Lighting

Landscape Lighting Services & Design: Create a website for our landscape lighting company. We would like the design to be tailored around this description:
Illuminate with Confidence. Designed with Precision. Installed with Care.
Locally and veteran-owned, we take pride in transforming outdoor spaces through innovative lighting solutions tailored to your vision. From landscape and holiday lighting to permanent installations, our effortless process and expert design deliver breathtaking results and lasting curb appeal. Backed by a lifetime warranty and quarterly service options, our commitment to quality and customer satisfaction is unwavering. Try before you buy and experience your home in a whole new light with our complimentary demo kit — see the stunning effects before you decide.
- Also, add in this information as well; Outdoor Lighting not only beautifies spaces but also significantly enhances safety by illuminating your home or business. Beautifully lit entrances deter potential intruders, making your home a safer place for your loved ones. we also offer quarterly service plans to ensure lighting equipment continues to operate & illuminate effectively throughout the year. Also mention we provide free estimates and we are offering a 10% discount to military, veterans, and first responders.

Target Market(s)

Luxury market

Industry/Entity Type

Landscape Lighting - Residential & Commercial Lighting Services

Coding

Coded - Design and coding required

Number of Pages Required

2 page

Colors
00AB8E
00BBA5
67D7C9
C6EFE9
E9F9F6
59FF00
82FF00
B8FF75
E3FFCB
F4FFEA
FFC000
F8CF3A
FAE287
FDF2CF
FEFAEE

Requirements
Must have
• a lead generation button where people can submit their information for us to reach out to them and schedule their free estimate, homepage, about page, contact page, products and services page, user friendly, easy to navigate, and it also must be engaging and eye popping, as well as appealing to the luxury market. Please use colors; verdent green, dark green, ivory, and sunny yellow. Also, include an about page that references our story; Glen is retired Army and he opened a fitness studio in 2017 with his wife Rosalind. He has installed low voltage lighting in every home he lived in and for his friends and family over the years and decided to open his own business because he is passionate about beautifying outdoor landscapes and highlighting a properties full potential, not only in the day but at night as well all while providing safety and security for his clients. Having a deep respect for nature and landscaping, he wants to provide the same care and quality to each of his clients as he has in the fitness industry for decades. He believes small businesses are the back bone of America and he's excited to provide a service that is all to often neglected in the design of a home.
Nice to have
• I would like to have a clear intent and purpose, engaging web design, clear call to action, optimized for search engines, mobile friendy design, security measures, credibility indicators

```html
<!DOCTYPE html>
<html lang="en">
<head>
<meta charset="utf-8">
<title>Corbel Crest Lighting — Landscape Lighting</title>
<link href="https://fonts.googleapis.com/css2?family=Poppins:wght@300;400;500;600;700;800&display=swap" rel="stylesheet">
<style>
:root{
  --forest:#0d3b2e;
  --forest-deep:#082a20;
  --verdant:#00ab8e;
  --verdant-mid:#00bba5;
  --verdant-light:#67d7c9;
  --verdant-soft:#e9f9f6;
  --lime:#82ff00;
  --lime-light:#b8ff75;
  --lime-soft:#f4ffea;
  --sun:#ffc000;
  --yellow:#f8cf3a;
  --yellow-light:#fae287;
  --yellow-soft:#fefaee;
  --ivory:#fffcf2;
  --ink:#1f2a25;
  --muted:#4f5a55;
  --footer:#0a2d23;
  --white:#fff;
}
*{margin:0;padding:0;box-sizing:border-box}
html,body{width:1200px;height:4398px;overflow:hidden}
body{position:relative;font-family:'Poppins',sans-serif;color:var(--ink);background:var(--white)}
.abs{position:absolute}
.btn{position:absolute;display:flex;align-items:center;justify-content:center;background:var(--yellow);color:var(--forest);font-weight:700;font-size:12.5px;text-transform:uppercase;border-radius:4px;letter-spacing:.2px;text-decoration:none;box-shadow:0 4px 10px rgba(0,0,0,.12)}

/* hero */
.hero{position:absolute;left:0;top:0;width:1200px;height:720px;overflow:hidden;
  background:
   radial-gradient(ellipse 260px 200px at 820px 300px,rgba(248,207,58,.55),transparent 75%),
   radial-gradient(ellipse 320px 260px at 900px 420px,rgba(0,171,142,.35),transparent 75%),
   linear-gradient(180deg,#114a39 0%,#0d3b2e 55%,#082a20 100%)}
.brand{position:absolute;font-weight:700;color:var(--yellow);text-transform:uppercase;letter-spacing:1px}
.hero .brand{left:89px;top:30px;font-size:22px;line-height:1.05}
.nav{position:absolute;top:29px;left:492px;height:36px;width:440px}
.nav a{color:var(--white);font-size:14px;text-decoration:none;position:absolute;white-space:nowrap}
.nav .active{background:var(--verdant);font-weight:700;font-size:13px;width:109px;height:36px;display:flex;align-items:center;justify-content:center;border-radius:2px;left:0;top:0}
.hero h1 .l1{position:absolute;left:89px;top:244px;font-size:38px;font-weight:700;color:var(--white);white-space:nowrap}
.hero h1 .l2{position:absolute;left:86px;top:290px;font-size:76px;font-weight:800;color:var(--white);white-space:nowrap;letter-spacing:1px}
.hero .tagline{left:89px;top:393px;font-size:19px;font-weight:700;color:var(--white);white-space:nowrap}
.hero .lead{left:89px;top:434px;width:520px;font-size:14px;font-weight:300;color:var(--white);line-height:1.6}
.mouse{left:1058px;top:612px}

.photo{position:absolute;border-radius:12px}
.h2{position:absolute;font-weight:800;color:var(--forest);text-transform:uppercase;line-height:1.05}
.sub-accent{position:absolute;font-weight:500;color:var(--verdant);text-transform:uppercase;font-size:16px}
.body-text{position:absolute;font-size:13px;font-weight:300;color:var(--muted);line-height:1.72}
.body-text p+p{margin-top:14px}

.expert{position:absolute;left:0;top:1314px;width:1200px;height:558px;background:var(--ivory)}
.feature{position:absolute;top:1535px;width:204px;height:254px;border-radius:8px;border:2px solid}
.feature .icon{position:absolute;left:53px;top:36px;width:97px;height:97px;border-radius:50%;display:flex;align-items:center;justify-content:center}
.feature .label{position:absolute;left:14px;right:14px;top:165px;text-align:center;font-size:13px;font-weight:500;text-transform:uppercase;color:var(--ink);line-height:1.55}

.discount{position:absolute;left:0;top:1872px;width:1200px;height:429px;
  background:radial-gradient(ellipse 500px 260px at 950px 80px,rgba(255,255,255,.07),transparent 70%),linear-gradient(180deg,#0f4535,#0b3529)}

.service{position:absolute;top:2979px;width:248px;height:290px;border-radius:14px;overflow:hidden;box-shadow:0 12px 28px rgba(8,42,32,.25)}
.service span{position:absolute;left:0;right:0;bottom:42px;text-align:center;color:var(--white);font-weight:700;font-size:21px;line-height:1.25;text-transform:uppercase}

.step-label{position:absolute;top:3706px;width:220px;text-align:center;font-size:16px;font-weight:700;text-transform:uppercase;line-height:1.4;color:var(--ink)}

.footer{position:absolute;left:0;top:3947px;width:1200px;height:451px;background:var(--footer)}
.f-head{position:absolute;color:var(--white);font-weight:700;font-size:14px;text-transform:uppercase}
.f-list{position:absolute;list-style:none;color:#e3ece8;font-size:13px}
.f-list li{height:26.5px}
.f-list li::before{content:"›";color:var(--yellow);margin-right:7px}
.f-text{position:absolute;color:#e3ece8;font-size:11.5px;line-height:1.5}
</style>
</head>
<body>

<header class="hero">
  <div class="abs" role="img" aria-label="Brick home with warm uplighting at dusk under tall trees" style="left:0;top:0;width:1200px;height:720px;background:radial-gradient(ellipse 300px 200px at 960px 260px,rgba(255,220,140,.22),transparent 70%)"></div>
  <div class="brand">Corbel Crest<br>Lighting</div>
  <nav class="nav">
    <a class="active" href="#">HOME</a>
    <a href="#" style="left:133px;top:9px">About</a>
    <a href="#" style="left:200px;top:9px">Services</a>
    <a href="#" style="left:284px;top:9px">Gallery</a>
    <a href="#" style="left:360px;top:9px">Contact</a>
  </nav>
  <a class="btn" href="#" style="left:947px;top:22px;width:163px;height:50px;font-size:13px">Free Estimate</a>
  <h1><span class="l1">ILLUMINATE WITH</span><span class="l2">CONFIDENCE</span></h1>
  <div class="abs tagline">DESIGNED WITH PRECISION. INSTALLED WITH CARE</div>
  <p class="abs lead">Transform your home or business with breathtaking outdoor lighting — tailored to your vision, installed with expert care.</p>
  <a class="btn" href="#" style="left:89px;top:500px;width:215px;height:51px">Get Your Free Estimate</a>
  <svg class="abs mouse" width="34" height="54" viewBox="0 0 34 54" aria-hidden="true">
    <rect x="1.5" y="1.5" width="31" height="51" rx="15" fill="none" stroke="#fff" stroke-width="2"/>
    <ellipse cx="17" cy="15" rx="4" ry="6" fill="none" stroke="#fff" stroke-width="1.8"/>
    <path d="M17 27v14M12 36l5 5 5-5" fill="none" stroke="#fff" stroke-width="1.8"/>
  </svg>
</header>

<section>
  <div class="photo" role="img" aria-label="Covered porch glowing with string lights at night" style="left:191px;top:831px;width:335px;height:446px;background:radial-gradient(ellipse 140px 110px at 60% 45%,#8a6a3c,transparent 75%),linear-gradient(180deg,#1c1a14,#23301f 60%,#141a12)"></div>
  <div class="photo" role="img" aria-label="Lit garden pathway leading to a gazebo at night" style="left:75px;top:881px;width:203px;height:307px;border:4px solid #fff;background:radial-gradient(ellipse 70px 60px at 55% 45%,#c98a5a,transparent 75%),linear-gradient(180deg,#1a2e3a,#1f3a2a 60%,#2a332e)"></div>
  <h2 class="h2" style="left:587px;top:908px;font-size:34px;width:460px">Light Up Beauty. Light Up Safety.</h2>
  <div class="body-text" style="left:588px;top:994px;width:450px">
    <p>Outdoor lighting isn’t just about making your property look stunning — it’s about making it feel secure.</p>
    <p>A beautifully lit home deters unwanted visitors, enhances nighttime visibility, and guides your family safely along walkways, driveways, and entry points.</p>
    <p>It’s where elegance meets protection — adding brilliance to your landscape while giving you the comfort of knowing your home is safe, stylish, and thoughtfully designed.</p>
  </div>
</section>

<section class="expert"></section>
<h2 class="h2" style="left:0;width:1200px;text-align:center;top:1368px;font-size:34px">Expert Outdoor Lighting</h2>
<div class="sub-accent" style="left:0;width:1200px;text-align:center;top:1416px">Services That Make An Impact</div>
<p class="body-text" style="left:240px;width:720px;text-align:center;top:1455px">From elegant landscape lighting to festive holiday displays and permanent architectural installations, we craft lighting solutions that blend beauty, safety, and performance.</p>

<div class="feature" style="left:166px;border-color:var(--verdant-light);background:linear-gradient(180deg,#e0f7f3,#fff)">
  <div class="icon" style="background:var(--verdant)">
    <svg width="46" height="46" viewBox="0 0 46 46" fill="none" stroke="#fff" stroke-width="2"><rect x="6" y="14" width="14" height="28"/><rect x="20" y="6" width="20" height="36"/><path d="M10 20h6M10 26h6M10 32h6M25 12h10M25 18h10M25 24h10M25 30h10M2 42h42"/></svg>
  </div>
  <div class="label">Residential and Commercial Projects</div>
</div>
<div class="feature" style="left:387px;border-color:#c6f59e;background:linear-gradient(180deg,#eefde0,#fff)">
  <div class="icon" style="background:var(--lime-light)">
    <svg width="46" height="46" viewBox="0 0 46 46" fill="none" stroke="#fff" stroke-width="2"><rect x="8" y="18" width="30" height="22"/><path d="M8 18l6-10h18l6 10M23 8v32M16 26h14"/></svg>
  </div>
  <div class="label">Free In-Home Demonstration Kit</div>
</div>
<div class="feature" style="left:609px;border-color:var(--yellow-light);background:linear-gradient(180deg,#fdf3d6,#fff)">
  <div class="icon" style="background:var(--yellow)">
    <svg width="46" height="46" viewBox="0 0 46 46" fill="none" stroke="#fff" stroke-width="2"><circle cx="23" cy="23" r="16"/><circle cx="23" cy="23" r="8"/><path d="M23 3v4M23 39v4M3 23h4M39 23h4M9 9l3 3M34 34l3 3M9 37l3-3M34 12l3-3"/></svg>
  </div>
  <div class="label">Veteran-Owned and Operated</div>
</div>
<div class="feature" style="left:830px;border-color:#4f7d6c;background:linear-gradient(180deg,#e4eee9,#fff)">
  <div class="icon" style="background:var(--forest)">
    <svg width="50" height="50" viewBox="0 0 50 50" fill="none" stroke="#fff" stroke-width="2"><circle cx="25" cy="25" r="20"/><circle cx="25" cy="25" r="13"/><path d="M19 31v-8h3l4-7c2 0 2 2 1 5h5c1 0 2 1 1 3l-2 6c0 1-1 1-2 1z"/></svg>
  </div>
  <div class="label">Lifetime Warranty + Quarterly Service Plans</div>
</div>

<section class="discount" role="img" aria-label="Deep green band over a faint brick house background"></section>
<svg class="abs" style="left:190px;top:1955px" width="270" height="270" viewBox="0 0 270 270" aria-hidden="true">
  <circle cx="135" cy="135" r="129" fill="none" stroke="#fff" stroke-width="5"/>
  <circle cx="135" cy="135" r="112" fill="#00ab8e"/>
</svg>
<div class="abs" style="left:222px;top:2008px;color:#fff;font-weight:800;font-size:100px;line-height:1;letter-spacing:-3px">10<span style="font-size:74px;letter-spacing:0">%</span></div>
<div class="abs" style="left:355px;top:2092px;color:#fff;font-weight:800;font-size:30px;line-height:1">OFF</div>
<div class="abs" style="left:238px;top:2132px;width:150px;height:36px;background:var(--yellow);color:var(--forest);font-weight:800;font-size:20px;display:flex;align-items:center;justify-content:center;border-radius:3px">DISCOUNT</div>
<h2 class="abs" style="left:580px;top:1996px;color:#fff;font-size:34px;font-weight:800">10% DISCOUNT</h2>
<p class="abs" style="left:582px;top:2054px;width:460px;color:#fff;font-size:17px;font-weight:400;line-height:1.55">For all military personnel, veterans, and first responders — our way of saying thank you.</p>
<a class="btn" href="#" style="left:582px;top:2127px;width:295px;height:51px">Free Estimates Always Available</a>

<div class="abs" role="img" aria-label="Outdoor dinner table under glowing string lights with lanterns on a lawn" style="left:654px;top:2301px;width:546px;height:521px;background:radial-gradient(ellipse 260px 90px at 50% 22%,rgba(255,210,130,.5),transparent 75%),linear-gradient(180deg,#3f4a36,#4f5a3a 45%,#2f3e22 75%,#26331c);box-shadow:-8px 10px 24px rgba(0,0,0,.25)"></div>
<h2 class="h2" style="left:94px;top:2399px;font-size:34px">About Us</h2>
<div class="sub-accent" style="left:94px;top:2447px;font-size:15px">A Veteran’s Vision, A Family’s Passion</div>
<div class="body-text" style="left:94px;top:2482px;width:490px">
  <p>Founded by Glen, a retired Army veteran, and his wife Rosalind, our company was born out of a love for lighting and a commitment to excellence. After years of lighting homes for friends and family, Glen decided to bring that same level of care to clients across the community.</p>
  <p>With deep respect for nature and years of experience running a successful fitness studio, Glen brings discipline, creativity, and heart into every project. We believe that lighting is the final touch that transforms your house into a home — safe, secure, and spectacular.</p>
</div>
<a class="btn" href="#" style="left:94px;top:2695px;width:176px;height:52px">Read Our Story</a>

<h2 class="h2" style="left:0;width:1200px;text-align:center;top:2909px;font-size:34px">Services We Offer</h2>
<div class="service" role="img" aria-label="Landscape lighting on a garden seating area" style="left:217px;background:linear-gradient(180deg,#4a6a3a 0%,#2d5a45 45%,#0d3b2e 100%)"><span>Landscape<br>Lighting</span></div>
<div class="service" role="img" aria-label="Warm holiday string lights" style="left:478px;background:linear-gradient(180deg,#3a2a10 0%,#b8842a 45%,#8a6a10 100%)"><span>Holiday<br>Lighting</span></div>
<div class="service" role="img" aria-label="Permanent outdoor lamp glowing at night" style="left:741px;background:radial-gradient(ellipse 60px 70px at 50% 25%,#eafff8,transparent 80%),linear-gradient(180deg,#2f6a5a 0%,#0f4a3a 60%,#0a3328 100%)"><span>Permanent<br>Installations</span></div>

<div class="abs" style="left:89px;top:3349px;width:1021px;height:1px;background:#d9d9d9"></div>

<h2 class="h2" style="left:0;width:1200px;text-align:center;top:3434px;font-size:34px">Our Process – Simple &amp; Effortless</h2>

<svg class="abs" style="left:91px;top:3514px" width="230" height="200" viewBox="0 0 230 200" aria-hidden="true">
  <path d="M26 100A84 84 0 0 1 191.6 80H215M209 74l6 6-6 6" fill="none" stroke="#b9dcd2" stroke-width="2"/><circle cx="26" cy="100" r="4" fill="#b9dcd2"/>
  <circle cx="110" cy="100" r="67" fill="#00ab8e"/>
  <g fill="none" stroke="#fff" stroke-width="2.2"><rect x="86" y="72" width="48" height="56" rx="3"/><rect x="94" y="80" width="32" height="12"/><path d="M94 100h6M106 100h6M118 100h6M94 110h6M106 110h6M118 110h6M94 120h30"/></g>
</svg>
<svg class="abs" style="left:347px;top:3514px" width="230" height="200" viewBox="0 0 230 200" aria-hidden="true">
  <path d="M26 100A84 84 0 0 0 191.6 120H215M209 114l6 6-6 6" fill="none" stroke="#b9dcd2" stroke-width="2"/><circle cx="26" cy="100" r="4" fill="#b9dcd2"/>
  <circle cx="110" cy="100" r="67" fill="#b8ff75"/>
  <g fill="none" stroke="#fff" stroke-width="2.4"><rect x="84" y="90" width="52" height="36"/><rect x="80" y="80" width="60" height="10"/><path d="M110 80v46M110 80c-6-12-18-12-16-2M110 80c6-12 18-12 16-2"/></g>
</svg>
<svg class="abs" style="left:602px;top:3514px" width="230" height="200" viewBox="0 0 230 200" aria-hidden="true">
  <path d="M26 100A84 84 0 0 1 191.6 80H215M209 74l6 6-6 6" fill="none" stroke="#b9dcd2" stroke-width="2"/><circle cx="26" cy="100" r="4" fill="#b9dcd2"/>
  <circle cx="110" cy="100" r="67" fill="#f8cf3a"/>
  <g fill="none" stroke="#fff" stroke-width="2.2"><rect x="82" y="80" width="50" height="44"/><path d="M90 116l8-10 8 6 10-14M112 110l24-30 6 5-24 30-8 3z"/></g>
</svg>
<svg class="abs" style="left:856px;top:3514px" width="230" height="200" viewBox="0 0 230 200" aria-hidden="true">
  <path d="M26 100A84 84 0 0 0 191.6 120H215M209 114l6 6-6 6" fill="none" stroke="#b9dcd2" stroke-width="2"/><circle cx="26" cy="100" r="4" fill="#b9dcd2"/>
  <circle cx="110" cy="100" r="67" fill="#0d3b2e"/>
  <g fill="none" stroke="#fff" stroke-width="2.2"><path d="M84 126c0-14 8-22 18-22s18 8 18 22"/><path d="M90 92a12 12 0 0 1 24 0v6M88 94v8h4v-8zM112 94v8h4v-8z"/><circle cx="128" cy="112" r="8"/><circle cx="128" cy="112" r="14" stroke-dasharray="4 3"/></g>
</svg>
<div class="step-label" style="left:91px">Free Estimate<br>Request</div>
<div class="step-label" style="left:347px">Complimentary<br>Demo Kit</div>
<div class="step-label" style="left:602px">Custom Design +<br>Installation</div>
<div class="step-label" style="left:856px">Ongoing<br>Support</div>

<footer class="footer">
  <div class="brand" style="left:145px;top:182px;font-size:30px;line-height:1.1;letter-spacing:1.5px">Corbel Crest<br>Lighting</div>

  <div class="f-head" style="left:400px;top:144px">Quick Links</div>
  <ul class="f-list" style="left:400px;top:178px">
    <li>Home</li><li>About</li><li>Services</li><li>Gallery</li><li>Contact</li>
  </ul>

  <div class="f-head" style="left:577px;top:144px">Contact Info</div>
  <svg class="abs" style="left:577px;top:178px" width="12" height="10" viewBox="0 0 12 10"><rect width="12" height="10" rx="1" fill="#f8cf3a"/><path d="M0 1l6 5 6-5" fill="none" stroke="#0a2d23" stroke-width="1.2"/></svg>
  <div class="f-text" style="left:597px;top:174px">Email:<br>hello@corbelcrestlighting.com</div>
  <svg class="abs" style="left:577px;top:227px" width="12" height="12" viewBox="0 0 24 24"><path d="M5 2h4l2 5-3 2a12 12 0 0 0 7 7l2-3 5 2v4a2 2 0 0 1-2 2A19 19 0 0 1 3 4a2 2 0 0 1 2-2z" fill="#f8cf3a"/></svg>
  <div class="f-text" style="left:597px;top:224px">Phone:<br>( 012 ) 555-0148</div>
  <svg class="abs" style="left:578px;top:285px" width="10" height="14" viewBox="0 0 10 14"><path d="M5 0a5 5 0 0 1 5 5c0 4-5 9-5 9S0 9 0 5a5 5 0 0 1 5-5z" fill="#f8cf3a"/><circle cx="5" cy="5" r="2" fill="#0a2d23"/></svg>
  <div class="f-text" style="left:597px;top:282px;width:200px">Location:<br>Corbel Crest Lighting 880 Lanternwood Drive, Cedar Hollow, TX 75000</div>

  <div class="f-head" style="left:855px;top:146px">Newsletter</div>
  <div class="f-text" style="left:855px;top:175px;width:210px">Subscribe to our email address to get the latest news.</div>
  <div class="abs" style="left:855px;top:230px;width:214px;height:43px;background:#16463a;border-radius:3px"></div>
  <svg class="abs" style="left:873px;top:247px" width="11" height="9" viewBox="0 0 12 10"><rect width="12" height="10" rx="1" fill="#f8cf3a"/><path d="M0 1l6 5 6-5" fill="none" stroke="#16463a" stroke-width="1.2"/></svg>
  <div class="f-text" style="left:891px;top:242px;color:#ddd">Enter Your Email...</div>
  <svg class="abs" style="left:1038px;top:244px" width="16" height="14" viewBox="0 0 16 14"><path d="M0 6L16 0 11 14 8 8z" fill="#f8cf3a"/></svg>

  <div class="abs" style="left:89px;top:394px;width:1021px;height:1px;background:#245446"></div>
  <div class="abs" style="left:0;width:1200px;top:415px;text-align:center;color:#e3ece8;font-size:12px">© COPYRIGHT 2025 &nbsp;| ALL RIGHTS RESERVED</div>
  <svg class="abs" style="left:1132px;top:374px" width="40" height="40" viewBox="0 0 40 40"><circle cx="20" cy="20" r="20" fill="#00ab8e"/><path d="M15 22l5-5 5 5" fill="none" stroke="#fff" stroke-width="2"/></svg>
</footer>

<section class="abs" style="left:131px;top:3850px;width:938px;height:160px;background:var(--verdant);border-radius:14px;box-shadow:0 10px 24px rgba(0,0,0,.2)">
  <h2 class="abs" style="left:44px;top:30px;color:#fff;font-size:48px;font-weight:800;white-space:nowrap;line-height:1.1">READY TO EXPERIENCE</h2>
  <div class="abs" style="left:46px;top:96px;color:#fff;font-size:22px;font-weight:700;white-space:nowrap">YOUR HOME IN A WHOLE NEW LIGHT?</div>
  <a class="btn" href="#" style="left:717px;top:54px;width:176px;height:51px">Read Our Story</a>
</section>

</body>
</html>
```